I need a newspaper ads that suits events / outings all over the world. refreshing feeling that suits my company logo.
Size of the ads is 6cm by 6cm a square
takenote
1) Joining up as members is free .
2) Places of interest tickets discount for members
3) Special events / outings host almost everyday
4) main point is everyone able to know each another
website : www.WanderNookly.com
Target Market(s)
Targeting general age 18-40 . mainly singles
contents to put inside the ads
2) Local Places of interest tickets discount for members
4) Website : www.WanderNookly.com
5) We also host photos contest
6) Meet the different faces of the world
7) Experience Sharing Gathering !
Industry/Entity Type
It Company
Requirements
Must have
- Refreshing feeling , and professional . will be uploading more pictures , kindly put some pictures combine into it to make people feel there is a lot activities can be involve when they join as member.

```html
<!DOCTYPE html>
<html lang="en">
<head>
<meta charset="utf-8">
<title>Halcyon Outings – Newspaper Ad</title>
<link rel="stylesheet" href="https://fonts.googleapis.com/css2?family=Cinzel:wght@600&family=Ubuntu:wght@500;700&display=swap">
<style>
  :root {
    --board: #ebebeb;
    --board-light: #f7f7f7;
    --sky-top: #2fa9e3;
    --sky-mid: #bfe6f7;
    --white: #ffffff;
    --brand: #1f86bd;
    --band-top: #0d4f8f;
    --band-bottom: #000000;
    --chip-ink: #111111;
    --chip-accent: #2a83b8;
    --swoosh-a: #1a7fd6;
    --swoosh-b: #0b3d9a;
    --photo-a: #6b7d6a;
    --photo-b: #3a3b3f;
  }
  * { margin: 0; padding: 0; box-sizing: border-box; }
  html, body { width: 1200px; height: 900px; overflow: hidden; }
  body {
    background: radial-gradient(ellipse at 50% 40%, var(--board-light), var(--board) 75%);
    font-family: "Ubuntu", sans-serif;
    position: relative;
  }
  .board-edge { position: absolute; left: 0; right: 0; height: 30px; background: var(--white); }
  .board-edge--top { top: 0; }
  .board-edge--bottom { bottom: 0; height: 28px; }

  .ad {
    position: absolute;
    width: 638px;
    height: 638px;
    overflow: hidden;
    background: var(--white);
    box-shadow: 6px 8px 10px rgba(0,0,0,0.45);
    transform-origin: top left;
  }
  .ad--colour { left: 22px; top: 140px; }
  .ad--mono {
    left: 667px; top: 247px;
    transform: scale(0.836);
    --sky-top: #8a8a8a;
    --sky-mid: #dcdcdc;
    --brand: #5a5a5a;
    --band-top: #4a4a4a;
    --band-bottom: #111111;
    --chip-accent: #6d6d6d;
    --swoosh-a: #bdbdbd;
    --swoosh-b: #4d4d4d;
    --photo-a: #9a9a9a;
    --photo-b: #3d3d3d;
  }

  .ad__sky {
    position: absolute; inset: 0 0 auto 0; height: 270px;
    background: linear-gradient(to bottom, var(--sky-top) 0%, var(--sky-mid) 28%, var(--white) 55%, var(--white) 100%);
  }

  .brand { position: absolute; left: 0; right: 0; top: 18px; text-align: center; }
  .brand__dot {
    display: block; margin: 0 auto 20px; width: 126px; height: 126px; border-radius: 50%;
    background: var(--brand);
  }
  .brand__name {
    font-family: "Cinzel", serif; font-weight: 600; color: var(--brand);
    font-size: 56px; line-height: 1; letter-spacing: 1px;
  }
  .brand__name span { display: block; font-size: 40px; letter-spacing: 20px; margin-top: 2px; padding-left: 20px; }

  .perks {
    position: absolute; left: 0; right: 0; top: 270px; height: 182px;
    background: linear-gradient(to bottom, var(--band-top), var(--band-bottom));
    list-style: none;
  }
  .perk {
    position: absolute; left: 90px; color: var(--white); font-weight: 700;
    font-size: 25px; line-height: 30px; white-space: nowrap;
  }
  .perk__num {
    position: absolute; top: -6px; width: 44px; height: 44px; border-radius: 50%;
    background: var(--white); color: var(--chip-ink); font-size: 30px; line-height: 44px; text-align: center;
  }
  .perk:nth-child(even) .perk__num { color: var(--chip-accent); }
  .perk:nth-child(1) { top: 10px; } .perk:nth-child(1) .perk__num { left: -78px; }
  .perk:nth-child(2) { top: 43px; } .perk:nth-child(2) .perk__num { left: -50px; }
  .perk:nth-child(3) { top: 78px; } .perk:nth-child(3) .perk__num { left: -76px; }
  .perk:nth-child(4) { top: 112px; } .perk:nth-child(4) .perk__num { left: -50px; }
  .perk__free { font-size: 32px; }

  .gallery { position: absolute; left: 0; right: 0; top: 452px; bottom: 0;
    background: linear-gradient(135deg, var(--swoosh-a), var(--swoosh-b) 45%, var(--swoosh-a) 70%, var(--swoosh-b)); }
  .gallery__photo {
    position: absolute; left: 86px; right: 72px; top: 4px; bottom: 0;
    background: linear-gradient(to bottom, var(--photo-a), var(--photo-b));
  }
</style>
</head>
<body>
  <div class="board-edge board-edge--top"></div>
  <div class="board-edge board-edge--bottom"></div>

  <article class="ad ad--colour">
    <div class="ad__sky"></div>
    <header class="brand">
      <i class="brand__dot"></i>
      <h1 class="brand__name">HALCYON<span>OUTINGS</span></h1>
    </header>
    <ol class="perks">
      <li class="perk"><span class="perk__num">1</span>Joining up as members is <span class="perk__free">free</span></li>
      <li class="perk"><span class="perk__num">2</span>Places of interest discount for members</li>
      <li class="perk"><span class="perk__num">3</span>Special events/outings host almost everyday</li>
      <li class="perk"><span class="perk__num">4</span>Main point is everyone able to know<br>each another</li>
    </ol>
    <div class="gallery">
      <div class="gallery__photo" role="img" aria-label="Group photo of young members smiling together on an outing"></div>
    </div>
  </article>

  <article class="ad ad--mono">
    <div class="ad__sky"></div>
    <header class="brand">
      <i class="brand__dot"></i>
      <h1 class="brand__name">HALCYON<span>OUTINGS</span></h1>
    </header>
    <ol class="perks">
      <li class="perk"><span class="perk__num">1</span>Joining up as members is <span class="perk__free">free</span></li>
      <li class="perk"><span class="perk__num">2</span>Places of interest discount for members</li>
      <li class="perk"><span class="perk__num">3</span>Special events/outings host almost everyday</li>
      <li class="perk"><span class="perk__num">4</span>Main point is everyone able to know<br>each another</li>
    </ol>
    <div class="gallery">
      <div class="gallery__photo" role="img" aria-label="Black and white group photo of young members smiling together on an outing"></div>
    </div>
  </article>
</body>
</html>
```